Corporate Travel Technology Company needs new Business Card design

We need a new business card design to reflect our re-branded company. Our company is called vendaXo (pronounced eureka) and we provide Business Intelligence and Corporate Trip Coordination solutions for the corporate travel industry. Our multinational customers use our solutions to manage large travel budgets and frequent travellers, as well as to save money and reduce risk. We'd like to see designs that use the blue and green palette as well as our corporate logo (attached below). The design should communicate innovation, insight, forward thinking, contemporary, trusted.

Target Market(s)

Large multinational corporates and Travel Agencies.

Industry/Entity Type

Business

Contact Information for Business Card

Marguerite Tallis
Chief Executive
vendaXo
Phone number - +61 (0)2 8147 3092
Email address - marguerite.tallis@vendaxo.example
Mobile number - +61 (0)455 206 718
www.vendaxo.example

Font styles to use
Other font styles liked:
• Please use font as close to corporate logo as possible

Colors
0255a3
0393ce
00a990
33b8a4
33a6d7
3176b5

Requirements
Must have
• Please include the words;
• Corporate Trip Coordination
• Sharpening Travel Spend Intelligence
• Use corporate logo - although icon can be stylised if needed

```html
<!DOCTYPE html>
<html lang="en">
<head>
<meta charset="utf-8">
<title>vendaXo business card</title>
<link rel="stylesheet" href="https://fonts.googleapis.com/css2?family=Open+Sans:wght@400;600;700&display=swap">
<style>
  :root {
    --page-bg: #e8e5e0;
    --card-dark: #56666a;
    --card-light: #ffffff;
    --brand-blue: #0ab0e8;
    --ink-slate: #4b5b60;
    --ink-grey: #5d6669;
    --rule-grey: #5f6b6e;
    --text-white: #ffffff;
  }
  html, body {
    margin: 0;
    width: 1200px;
    height: 950px;
    overflow: hidden;
    background: var(--page-bg);
    font-family: "Open Sans", Arial, sans-serif;
  }
  .canvas {
    position: relative;
    width: 1200px;
    height: 950px;
  }
  .card {
    position: absolute;
    width: 700px;
    height: 400px;
    box-shadow: 0 10px 28px rgba(0,0,0,0.25);
    overflow: hidden;
  }
  /* Back side */
  .card-back {
    left: 120px;
    top: 50px;
    background: var(--card-dark);
  }
  .back-brand {
    position: absolute;
    left: 0;
    right: 0;
    top: 120px;
    display: flex;
    justify-content: center;
    align-items: center;
    gap: 18px;
  }
  .brand-dot {
    width: 44px;
    height: 44px;
    border-radius: 50%;
    background: var(--brand-blue);
  }
  .back-brand .brand-name {
    font-size: 64px;
    font-weight: 400;
    color: var(--brand-blue);
    letter-spacing: 1px;
    line-height: 1;
  }
  .tagline {
    position: absolute;
    left: 0;
    right: 0;
    bottom: 58px;
    margin: 0;
    text-align: center;
    font-size: 17px;
    color: var(--text-white);
    letter-spacing: 0.3px;
    white-space: nowrap;
  }
  .tagline .sep {
    color: var(--brand-blue);
    margin: 0 6px;
  }
  /* Front side */
  .card-front {
    left: 380px;
    top: 500px;
    background: var(--card-light);
  }
  .wave {
    position: absolute;
    inset: 0;
  }
  .front-brand {
    position: absolute;
    right: 40px;
    top: 40px;
    display: flex;
    align-items: center;
    gap: 14px;
  }
  .front-brand .brand-dot {
    width: 34px;
    height: 34px;
  }
  .front-brand .brand-name {
    font-size: 58px;
    font-weight: 400;
    color: var(--ink-slate);
    line-height: 1;
  }
  .contacts {
    position: absolute;
    right: 34px;
    top: 150px;
    margin: 0;
    padding: 0;
    list-style: none;
    font-size: 15px;
    color: var(--ink-grey);
    text-align: right;
  }
  .contacts li {
    display: flex;
    justify-content: flex-end;
    align-items: center;
    gap: 10px;
    height: 23px;
  }
  .contacts svg {
    width: 14px;
    height: 14px;
    flex: none;
  }
  .person {
    position: absolute;
    left: 60px;
    bottom: 42px;
    color: var(--text-white);
  }
  .person-name {
    margin: 0;
    font-size: 26px;
    font-weight: 700;
  }
  .person-role {
    margin: 2px 0 0;
    font-size: 18px;
    font-weight: 400;
  }
</style>
</head>
<body>
<main class="canvas">
  <section class="card card-back">
    <div class="back-brand">
      <span class="brand-dot"></span>
      <span class="brand-name">vendaXo</span>
    </div>
    <p class="tagline">Corporate Trip Coordination<span class="sep">•</span>Sharpening Travel Spend Intelligence</p>
  </section>

  <section class="card card-front">
    <svg class="wave" viewBox="0 0 700 400" width="700" height="400" aria-hidden="true">
      <path d="M0,118 C30,170 130,205 270,214 C390,222 430,300 472,400 L0,400 Z" fill="var(--brand-blue)"/>
      <path d="M0,104 C30,156 130,192 270,201 C395,209 440,300 486,400" fill="none" stroke="var(--rule-grey)" stroke-width="4"/>
    </svg>

    <div class="front-brand">
      <span class="brand-dot"></span>
      <span class="brand-name">vendaXo</span>
    </div>

    <ul class="contacts">
      <li>+61 (0)2 8147 3092
        <svg viewBox="0 0 14 14"><circle cx="7" cy="7" r="7" fill="var(--brand-blue)"/><path d="M4 4h2l.6 2-1 .7a5 5 0 0 0 2.7 2.7l.7-1 2 .6v2A6.5 6.5 0 0 1 4 4z" fill="#fff"/></svg>
      </li>
      <li>+61 (0)455 206 718
        <svg viewBox="0 0 14 14"><rect x="3.5" y="1" width="7" height="12" rx="1.5" fill="var(--brand-blue)"/><rect x="4.8" y="2.5" width="4.4" height="7.5" fill="#fff"/></svg>
      </li>
      <li>marguerite.tallis@vendaxo.example
        <svg viewBox="0 0 14 14"><rect x="1" y="3" width="12" height="8" rx="1" fill="var(--brand-blue)"/><path d="M1.5 3.5 7 8l5.5-4.5" fill="none" stroke="#fff" stroke-width="1.2"/></svg>
      </li>
      <li>www.vendaxo.example
        <svg viewBox="0 0 14 14"><circle cx="7" cy="7" r="6.5" fill="var(--brand-blue)"/><path d="M1 7h12M7 .8c-3 3.5-3 8.9 0 12.4M7 .8c3 3.5 3 8.9 0 12.4" fill="none" stroke="#fff" stroke-width="1"/></svg>
      </li>
    </ul>

    <div class="person">
      <h1 class="person-name">Marguerite Tallis</h1>
      <p class="person-role">Chief Executive</p>
    </div>
  </section>
</main>
</body>
</html>
```